Premium Label Design for Sleep Supplement Targeted at Shift Workers (Vendora Launch)

🧠 PROJECT OVERVIEW

We are launching a premium dietary supplement brand on Vendora called:

Lumen Crestworks

The product is:

DuskaHush – Shift Work Sleep & Recovery Formula

This supplement is specifically designed for shift workers (nurses, emergency responders, aviation crew, rotating schedule professionals) who struggle with irregular sleep cycles.

This is NOT a generic sleep supplement.
It is a targeted recovery solution.

The label must feel:

• Premium
• Modern
• Professional
• Performance-oriented
• Clean
• Vendora-ready

No clutter. No generic wellness design.

🎯 TARGET AUDIENCE

Primary:
Shift workers aged 25–55

Examples:
• Nurses
• Paramedics
• Aviation crew
• FIFO workers
• Rotating schedule professionals

These are responsible professionals.
The design must reflect trust and authority.

📦 PRODUCT DETAILS (FRONT LABEL ONLY)

Bottle Colour:
White plastic bottle

Label Type:
Wrap-around label

Primary Front Text (Hierarchy Matters):

1️⃣ Lumen Crestworks Logo
2️⃣ DuskaHush (moon crescent icon incorporated on the letter "g", if possible. This is desirable as it makes the text look unique.
3️⃣ Shift Work Sleep Support Formula
4️⃣ Also ideal for travel & irregular schedules -
Supports Circadian Rhythm, Restorative Sleep and Recovery*
5️⃣ 60 Capsules | 30-Day Supply

Include a small badge that reads:

Recommended by Airline Professionals (badge icon or text). Icon preferably, on the top corner of the bottle or anywhere it can be noticed.

🎨 DESIGN DIRECTION (VERY IMPORTANT)

The design should feel:

Premium Performance Recovery
Modern Minimalist
Night-Aligned
Structured

Primary colour direction:

Deep midnight navy gradient
Top: #142A4A
Bottom: #081428

or a colour of your choice

Accent colours should be minimal.

Avoid bright green, neon, pastel, or spa-like tones.

❌ WHAT WE DO NOT WANT

No:
• Cheap private-label look
• Too much white

This must look like a serious modern supplement brand.

🧱 LAYOUT PREFERENCES

Strong top section with dark gradient band.

Product name (DuskaHush) must dominate.

Brand (Lumen Crestworks) must be present but secondary.

Shift Work Sleep Support Formula must be clear and confident.

Use white space intentionally.

Typography should be clean, modern sans-serif.

📐 VENDORA CONSIDERATIONS

The label must:

• Be readable at thumbnail size
• Have clear text hierarchy
• Not look cluttered
• Stand out in a crowded sleep supplement category
• Feel more premium than competitors

🏆 WINNING DESIGN WILL BE

• Modern and confident
• Clearly targeted
• Minimal but strong
• Professional
• Scalable to future products

📁 FILE REQUIREMENTS

Final files must include:

• AI or vector source files
• High-resolution print-ready files
• Editable files
• Font details

- Label Template is attached - this is supplied by the manufacturer to edit. Modify it in any way you like to suit the design style.

- Certificates are attached and can be modified to suit label design theme ( I require all three certificates to be displayed - if you have better quality stock vector icons for the certificates please use those as you desire, but they must be placed. Doesn't have to be exactly as the ones I have supplied. They don't have to be on the front label either.

- Stock vector icons for - NON-GMO or GMO Free, No Artificial Additives, Non-Habit Forming and Herbal Extract Blend - must be included - it doesn't have to be on the front label though.

- Lumen Crestworks Logo is Provided.

On Supplement Fact Label Section, please include -
Manufactured for and distributed by:
LUMEN CRESTWORKS - USE TEXT LOGO PROVIDED
4718 Harbor Vale Road, Suite 112 PMB 947
Dallas, TX 75019 United States

-UPC code needs to be placed on label. It can be altered to suit label. Use the guidelines on this website ;
https://help.codemintery.example/en/guides/articles/49000037215-resizing-your-barcode-artwork

LUMEN CRESTWORKS Logo font is Open Sans Light LUMEN is in Bold.

Ideally, I would like some white stars on the label.

I have attached some specific things I like so far from the submissions to the brief -please try to incorporate these as closely as possible.

-----UPDATE-----

Thank you all for your submissions.

I have come up with a sample design using AI and this is what I want you to work with as an example. The image we just generated is a raster mockup (PNG).
It is not a true vector file, so it cannot simply be converted into a clean professional Illustrator (.AI) file without rebuilding it properly. Please rebuild the entire 6" x 2.5" label as:

• True vector layout
• Fully editable
• Proper CMYK setup
• 300 DPI
• 0.125" bleed
• Correct safe margins
• Separate layers
• Editable text (Open Sans family)
• Vector icons
• Proper Supplement Facts formatting

That means I will get a real production-ready Illustrator file, not a traced image. The designer who can produce this will be the winner. Please note, icons are not correct. This is for visual guidance only. Please follow all instructions as per the brief provided. I look forward to your submissions and working with you on this project.

Target Market(s)

Shift Workers who are willing to pay a premium for a sleep aid/supplement

Industry/Entity Type

• Nurses • Paramedics • Aviation crew • FIFO workers • Rotating schedule professionals

Colors

Designer to choose colors to be used in the design.

Requirements
Must have
• As per brief - icons (NON-GMO or GMO Free, No Artificial Additives, Non-Habit Forming and Herbal Extract Blend), stars, moon image incorporated onto the "g" letter of DuskaHush (image attached for ideas), recommended by Airline Crew (preferably an Icon), Certificates (uploaded) can be customised to suit label from your own vectors.
Nice to have
• As per brief
Should not have
• As per brief

```html
<!DOCTYPE html>
<html lang="en">
<head>
<meta charset="utf-8">
<title>DuskaHush – Shift Work Sleep Support Formula</title>
<link rel="stylesheet" href="https://fonts.googleapis.com/css2?family=Open+Sans:wght@400;600;700;800&family=Oswald:wght@500;600&display=swap">
<style>
  :root {
    --navy: #0d1b45;
    --white: #ffffff;
    --paper: #f2f2f5;
    --ribbon: #d4040a;
    --ribbon-light: #ff3d3d;
    --ribbon-dark: #8f1114;
    --cyan: #1aa6e0;
    --violet: #8e3bb8;
    --orange: #f07b1f;
    --supply-blue: #1b8fe0;
    --divider: #b8c4d4;
  }
  * { margin: 0; padding: 0; box-sizing: border-box; }
  html, body { width: 1200px; height: 1200px; overflow: hidden; background: var(--white); }
  .canvas { position: relative; width: 1200px; height: 1200px; background: var(--white); font-family: "Open Sans", sans-serif; }

  .label-panel {
    position: absolute; left: 287px; top: 330px; width: 632px; height: 820px;
    background: var(--paper); border-radius: 28px;
  }

  .ribbon-fold {
    position: absolute; left: 256px; top: 300px; width: 32px; height: 94px;
    background: var(--ribbon-dark);
    clip-path: polygon(0 0, 100% 0, 100% 100%, 0 72%);
  }
  .launch-ribbon {
    position: absolute; left: 256px; top: 250px; width: 556px; height: 82px;
    background: linear-gradient(90deg, var(--ribbon-light), var(--ribbon) 35%, var(--ribbon));
    transform: rotate(-20deg); transform-origin: left top;
    border-radius: 0 8px 8px 0;
    display: flex; align-items: center; justify-content: center;
  }
  .launch-ribbon span {
    font-family: "Oswald", sans-serif; font-weight: 600; font-size: 54px;
    color: var(--white); line-height: 1; white-space: nowrap; letter-spacing: 0.5px;
  }

  .brand-name {
    position: absolute; left: 0; width: 1208px; top: 372px; text-align: center;
    font-weight: 700; color: var(--navy); font-size: 40px; letter-spacing: 8px; line-height: 1;
  }
  .brand-name .sub { display: block; margin-top: 10px; font-size: 17px; font-weight: 600; letter-spacing: 17px; }

  .product-name {
    position: absolute; left: 0; width: 1212px; top: 462px; text-align: center;
    font-weight: 700; color: var(--navy); font-size: 100px; letter-spacing: -1px; line-height: 1;
  }

  .night-sky { position: absolute; left: 300px; top: 562px; width: 606px; height: 372px; }

  .claim {
    position: absolute; left: 0; width: 1208px; text-align: center; white-space: nowrap;
    display: flex; align-items: center; justify-content: center; gap: 12px;
    color: var(--white); font-family: "Oswald", sans-serif; font-weight: 500; line-height: 1;
    text-shadow: 0 2px 3px rgba(10,10,40,0.85);
  }
  .claim::before, .claim::after { content: ""; width: 26px; height: 2px; background: var(--white); }
  .claim-lead { top: 756px; font-size: 30px; font-weight: 600; }
  .claim-note { top: 798px; font-size: 19px; }
  .claim-detail { top: 838px; font-size: 19px; }
  .claim-detail-end { top: 862px; font-size: 19px; }
  .claim-detail-end::before, .claim-detail-end::after { display: none; }

  .ingredient {
    position: absolute; top: 944px; height: 44px; border-radius: 22px; border: 2.5px solid;
    display: flex; align-items: center; justify-content: center;
    font-size: 22px; font-weight: 600; color: var(--navy); letter-spacing: 0.3px; background: var(--paper);
  }
  .ingredient.melatonin { left: 337px; width: 161px; border-color: var(--cyan); }
  .ingredient.gaba { left: 528px; width: 114px; border-color: var(--violet); }
  .ingredient.tryptophan { left: 672px; width: 199px; border-color: var(--orange); }

  .count { position: absolute; left: 0; width: 1208px; top: 996px; display: flex; justify-content: center; align-items: baseline; gap: 16px; color: var(--navy); line-height: 1; }
  .count-number { font-size: 58px; font-weight: 700; }
  .count-unit { font-size: 22px; font-weight: 600; }

  .supply { position: absolute; left: 0; width: 1210px; top: 1063px; text-align: center; color: var(--supply-blue); font-size: 22px; font-weight: 600; letter-spacing: 0.5px; line-height: 1; }
  .supply .divider { color: var(--divider); font-weight: 400; margin: 0 6px; }
</style>
</head>
<body>
<div class="canvas">
  <div class="label-panel"></div>

  <div class="ribbon-fold"></div>
  <div class="launch-ribbon"><span>VENDORA LAUNCH SALE</span></div>

  <div class="brand-name">LUMEN<span class="sub">CRESTWORKS</span></div>

  <div class="product-name">DuskaHush</div>

  <svg class="night-sky" viewBox="0 0 606 372" role="img" aria-label="Illustration of a crescent moon and stars in a purple night sky above soft pink clouds">
    <defs>
      <radialGradient id="skyGlow" cx="50%" cy="40%" r="62%">
        <stop offset="0%" stop-color="#3f3290"/>
        <stop offset="55%" stop-color="#5840a6"/>
        <stop offset="85%" stop-color="#9a78c8" stop-opacity="0.75"/>
        <stop offset="100%" stop-color="#f2f2f5" stop-opacity="0"/>
      </radialGradient>
      <linearGradient id="cloudBand" x1="0" y1="0" x2="0" y2="1">
        <stop offset="0%" stop-color="#6a4fb8" stop-opacity="0"/>
        <stop offset="60%" stop-color="#b888d0" stop-opacity="0.6"/>
        <stop offset="100%" stop-color="#e3b0c8" stop-opacity="0.85"/>
      </linearGradient>
      <linearGradient id="horizonArc" x1="0" y1="0" x2="1" y2="0">
        <stop offset="0%" stop-color="#f07b1f"/>
        <stop offset="35%" stop-color="#f5a623"/>
        <stop offset="55%" stop-color="#8e3bb8"/>
        <stop offset="75%" stop-color="#1aa6e0"/>
        <stop offset="100%" stop-color="#3a5fc8"/>
      </linearGradient>
      <clipPath id="skyClip">
        <path d="M22 40 Q303 -20 584 40 L606 290 Q303 420 0 290 Z"/>
      </clipPath>
    </defs>
    <g clip-path="url(#skyClip)">
      <rect width="606" height="372" fill="url(#skyGlow)"/>
      <rect y="150" width="606" height="222" fill="url(#cloudBand)"/>
    </g>
    <path d="M0 290 Q303 432 606 288 Q303 404 0 290 Z" fill="url(#horizonArc)"/>
  </svg>

  <div class="claim claim-lead">SHIFT WORK SLEEP SUPPORT FORMULA</div>
  <div class="claim claim-note">ALSO IDEAL FOR TRAVEL &amp; IRREGULAR SCHEDULES *</div>
  <div class="claim claim-detail">SUPPORTS CIRCADIAN RHYTHM, RESTORATIVE</div>
  <div class="claim claim-detail-end">SLEEP &amp; RECOVERY *</div>

  <div class="ingredient melatonin">MELATONIN</div>
  <div class="ingredient gaba">GABA</div>
  <div class="ingredient tryptophan">L-TRYPTOPHAN</div>

  <div class="count"><span class="count-number">60</span><span class="count-unit">CAPSULES</span></div>

  <div class="supply">DIETARY SUPPLEMENT<span class="divider">|</span>30 DAY SUPPLY</div>
</div>
</body>
</html>
```